Postcard Coupon Design

Local bar "The Dapple" we have great food, BBQ, wings, burgers, I would like to incorporate on the back company information such as happy hours, food specials,
and on the front a nice BBQ picture with some wings, and the following offers
"Free wings with any pitcher of regular priced beer"
"$5 off any check of $25 or more"
"Buy one get one free sandwiches 11am-3pm"
"Buy one get one free Appetizers"
The following on the back
"One coupon per customer per day, not to be combined with any other offers"
Check us out on Hopgrove.com
www.thedapple.com
happy hour 4-6pm M-F all beers and mixed drinks on special!
555-248-7130
218 Kestle Avenue
Phoenixville, PA 19872

Industry/Entity Type

It Company

Font styles to use
Serif
Sans Serif

Colors

Designer to choose colors to be used in the design.

```html
<!DOCTYPE html>
<html lang="en">
<head>
<meta charset="utf-8">
<title>The Dapple – Postcard Coupon</title>
<link href="https://fonts.googleapis.com/css2?family=Tinos:wght@400;700&display=swap" rel="stylesheet">
<style>
  :root {
    --bg: #000000;
    --gold: #dcb24a;
    --gold-light: #f6e08a;
    --gold-mid: #c9a02e;
    --gold-dark: #8a6814;
    --meat-dark: #3a1a12;
    --meat-red: #9a3a34;
    --meat-pink: #c96a66;
    --wing-brown: #6b3a1a;
    --wing-red: #b3231c;
  }
  html, body { margin: 0; padding: 0; overflow: hidden; background: var(--bg); }
  .postcard {
    position: relative;
    width: 851px;
    height: 1200px;
    background: var(--bg);
    color: var(--gold);
    font-family: "Tinos", "Times New Roman", serif;
    font-weight: 700;
    overflow: hidden;
  }
  .brand-name {
    position: absolute;
    left: 6px; top: 58px; width: 354px;
    margin: 0;
    text-align: center;
    font-size: 64px;
    line-height: 1;
    color: var(--gold);
  }
  .tagline {
    position: absolute;
    left: 420px; top: 24px; width: 400px;
    margin: 0;
    text-align: center;
    font-size: 37px;
    line-height: 70px;
  }
  .happy-hour {
    position: absolute;
    left: 0; top: 233px; width: 840px;
    margin: 0;
    text-align: center;
    font-size: 25px;
    line-height: 35px;
    text-transform: uppercase;
  }
  .frame {
    position: absolute;
    box-sizing: border-box;
    background: linear-gradient(135deg, var(--gold-light), var(--gold-mid) 35%, var(--gold-light) 55%, var(--gold-dark) 80%, var(--gold-mid));
    box-shadow: inset 0 0 0 2px var(--gold-dark);
  }
  .frame::before {
    content: "";
    position: absolute;
    box-sizing: border-box;
    border: 3px solid var(--gold-dark);
    background: linear-gradient(315deg, var(--gold-light), var(--gold-mid) 50%, var(--gold-light));
  }
  .frame--brisket { left: 34px; top: 356px; width: 398px; height: 278px; }
  .frame--brisket::before { left: 30px; top: 32px; right: 30px; bottom: 32px; }
  .frame--wings { left: 538px; top: 737px; width: 278px; height: 247px; }
  .frame--wings::before { left: 30px; top: 32px; right: 30px; bottom: 16px; }
  .photo { position: absolute; }
  .photo--brisket {
    left: 44px; top: 46px; width: 312px; height: 188px;
    background: radial-gradient(ellipse at 55% 45%, var(--meat-pink), var(--meat-red) 45%, var(--meat-dark) 90%);
  }
  .photo--wings {
    left: 43px; top: 45px; width: 189px; height: 172px;
    background: radial-gradient(ellipse at 55% 55%, var(--wing-brown), #3a1d0c 60%, var(--wing-red) 95%);
  }
  .offer { position: absolute; margin: 0; text-align: center; }
  .offer--appetizers { left: 440px; top: 432px; width: 400px; font-size: 22px; }
  .offer--wings-title { left: 420px; top: 612px; width: 400px; font-size: 44px; }
  .offer--wings-note { left: 380px; top: 667px; width: 470px; font-size: 22px; }
  .offer-list {
    position: absolute;
    left: 20px; top: 752px; width: 532px;
    margin: 0; padding: 0; list-style: none;
    text-align: center;
    font-size: 22px;
  }
  .offer-list li { height: 60px; }
  .contact {
    position: absolute;
    left: 0; top: 1126px; width: 851px;
    margin: 0;
    text-align: center;
    font-weight: 400;
    font-size: 13px;
    line-height: 19px;
  }
</style>
</head>
<body>
<main class="postcard">
  <h1 class="brand-name">The Dapple</h1>

  <p class="tagline">Your Oask<br>Neighborhood Tavern<br>for 60 years</p>

  <p class="happy-hour">Happy Hour<br>4-6pm M-F<br>All beers and mixed drinks on special</p>

  <div class="frame frame--brisket">
    <div class="photo photo--brisket" role="img" aria-label="Sliced smoked BBQ brisket"></div>
  </div>

  <p class="offer offer--appetizers">Buy one get one free Appetizers</p>

  <p class="offer offer--wings-title">Free wings</p>
  <p class="offer offer--wings-note">with any pitcher of regular priced beer</p>

  <ul class="offer-list">
    <li>$5 off any check of $25 or more</li>
    <li>Buy one get one free sandwiche 11am-3pm</li>
    <li>The following on the back</li>
  </ul>

  <div class="frame frame--wings">
    <div class="photo photo--wings" role="img" aria-label="Plate of glazed BBQ chicken wings"></div>
  </div>

  <address class="contact">
    555-248-7130<br>
    218 Kestle Ave. ,Phoenixville, PA 19872<br>
    www.thedapple.com
  </address>
</main>
</body>
</html>
```